Business Card Design Project

We need a business card design for a new boutique consulting company, TivaConsulting. Our new logo has just been designed and we are looking for simple, clean looking business cards. Logo attached

Industry/Entity Type

Boutique

Requirements
Must have
• There must be room for each card to have the following details:
Name
Title
Address - 2 lines
Phone number
Email address
Website address

Nice to have
• May have something on the back of the buisness card - emphasing the word "Tiva".

```html
<!DOCTYPE html>
<html lang="en">
<head>
<meta charset="utf-8">
<title>TivaConsulting – Business Cards</title>
<link rel="stylesheet" href="https://fonts.googleapis.com/css2?family=Open+Sans:wght@400;600&display=swap">
<style>
  :root {
    --paper: #ffffff;
    --frame: #333333;
    --card-edge: #222222;
    --ink: #4a4a4a;
    --brand-grey: #8a8a8a;
    --mark-grey: #e2e2e2;
    --green-light: #9fd66a;
    --green-dark: #3fae3a;
    --shadow: rgba(0, 0, 0, 0.55);
  }
  * { box-sizing: border-box; margin: 0; padding: 0; }
  html, body { width: 1200px; height: 849px; overflow: hidden; background: var(--paper); }
  .sheet {
    position: relative;
    width: 1200px;
    height: 849px;
    border: 1.5px solid var(--frame);
    background: var(--paper);
    font-family: "Open Sans", Arial, sans-serif;
  }
  .card {
    position: absolute;
    width: 470px;
    height: 287px;
    background: var(--paper);
    border: 1.5px solid var(--card-edge);
    box-shadow: 8px 8px 7px var(--shadow);
    overflow: hidden;
  }
  .card--front { left: 60px; top: 277px; }
  .card--back { left: 684px; top: 280px; width: 475px; }

  .brand {
    position: absolute;
    left: 4px;
    top: 112px;
    display: flex;
    align-items: center;
    gap: 10px;
  }
  .brand__square {
    width: 24px;
    height: 24px;
    background: var(--brand-grey);
  }
  .brand__name {
    font-size: 61px;
    font-weight: 400;
    letter-spacing: -1.5px;
    line-height: 1;
    color: var(--brand-grey);
  }

  .contact {
    position: absolute;
    left: 48px;
    top: 64px;
    list-style: none;
    font-size: 15.5px;
    line-height: 20.6px;
    color: var(--ink);
  }
  .back-mark {
    position: absolute;
    left: 290px;
    top: 24px;
    width: 130px;
    height: 140px;
    background: var(--mark-grey);
  }
  .band {
    position: absolute;
    left: 0;
    right: 0;
    bottom: 0;
    height: 67px;
    background: linear-gradient(to bottom, var(--green-light), var(--green-dark));
  }
</style>
</head>
<body>
  <main class="sheet">
    <section class="card card--front" aria-label="Card front">
      <div class="brand">
        <span class="brand__square" aria-hidden="true"></span>
        <span class="brand__name">TivaConsulting</span>
      </div>
    </section>

    <section class="card card--back" aria-label="Card back">
      <span class="back-mark" aria-hidden="true"></span>
      <ul class="contact">
        <li>Mara Ellison</li>
        <li>Senior Consultant</li>
        <li>24 Harbour Lane</li>
        <li>Northvale 2000</li>
        <li>09 4152 6081</li>
        <li>www.tivaconsulting.com</li>
        <li>mara@tivaconsulting.com</li>
      </ul>
      <div class="band" aria-hidden="true"></div>
    </section>
  </main>
</body>
</html>
```